Bref créative
VerdaLune
Business Cards etc...
Professional
Carmen Delvoe
Owner
3284-B Willow Crest Rd. #261
Greensboro, NC 27490
verdalunenc@mailbox.example
www.VerdaLuneNC.example
Landscape Management Services
Striving for earth friendly services
Member of 2% Pour Le Sol, Has a logo
landscaping | hardscapes | lighting | irrigation | water features | design | walls | patios | contract lawncare |

```html
<!DOCTYPE html>
<html lang="en">
<head>
<meta charset="utf-8">
<title>VerdaLune Stationery</title>
<link rel="stylesheet" href="https://fonts.googleapis.com/css2?family=Montserrat:wght@700;800&family=Roboto:wght@400;500;700&display=swap">
<style>
  :root{
    --green:#4a9a2c;
    --green-dark:#2f6f1c;
    --green-light:#9fcc7a;
    --green-pale:#e7f1de;
    --paper:#ffffff;
    --ink:#3a3a3a;
    --grey:#777;
    --bg:#d9c7a6;
  }
  *{box-sizing:border-box;margin:0;padding:0}
  html,body{width:1200px;height:504px;overflow:hidden}
  body{background:var(--bg);font-family:"Roboto",Arial,sans-serif;color:var(--ink);position:relative}
  .item{position:absolute;background:var(--paper);overflow:hidden;box-shadow:0 1px 3px rgba(0,0,0,.25)}
  .card{width:192px;height:96px;border-radius:4px}
  .wordmark{font-family:"Montserrat",Arial,sans-serif;font-weight:800;color:var(--green-dark);display:flex;align-items:center;gap:4px;line-height:1}
  .wordmark .dot{width:.8em;height:.8em;border-radius:50%;background:var(--green)}
  .tagline{font-size:4px;letter-spacing:.3px;color:var(--green);text-transform:uppercase;font-weight:700}
  .wave{position:absolute;left:0;bottom:0;width:100%}
  .name{font-size:8px;font-weight:700;color:var(--green-dark)}
  .role{font-size:5px;color:var(--grey)}
  .contact{font-size:4.6px;line-height:7px;color:var(--ink)}
  .contact i{display:inline-block;width:4px;height:4px;border-radius:50%;background:var(--green);margin-right:3px;vertical-align:middle}
  .services{font-size:5px;color:#fff;line-height:8px}
  .checklist{list-style:none;font-size:4.8px;line-height:8px}
  .checklist li::before{content:"";display:inline-block;width:4px;height:4px;border:.8px solid currentColor;margin-right:4px;vertical-align:middle}
  .emblem{border-radius:50%;position:absolute}
  .web{font-size:5px;font-weight:700}
</style>
</head>
<body>

<!-- Card: front A -->
<div class="item card" style="left:19px;top:60px">
  <div style="position:absolute;left:10px;top:8px">
    <div class="wordmark" style="font-size:17px"><span class="dot"></span>VerdaLune</div>
    <div class="tagline" style="margin:2px 0 0 17px">Landscape Management Services</div>
  </div>
  <div style="position:absolute;left:10px;top:42px">
    <div class="name">Carmen Delvoe</div>
    <div class="role">Owner</div>
  </div>
  <div class="contact" style="position:absolute;left:104px;top:36px">
    3284-B Willow Crest Rd. #261<br>Greensboro, NC 27490<br><i></i>(336) 555-0142<br><i></i>verdalunenc@mailbox.example<br><i></i>www.VerdaLuneNC.example
  </div>
  <svg class="wave" viewBox="0 0 192 18" height="18" preserveAspectRatio="none"><path d="M0 8 Q96 -2 192 8 V18 H0Z" fill="var(--green)"/></svg>
</div>

<!-- Card: front B -->
<div class="item card" style="left:228px;top:60px">
  <div style="position:absolute;left:10px;top:8px">
    <div class="wordmark" style="font-size:17px"><span class="dot"></span>VerdaLune</div>
    <div class="tagline" style="margin:2px 0 0 17px">Landscape Management Services</div>
  </div>
  <div style="position:absolute;left:10px;top:44px">
    <div class="name">Carmen Delvoe</div>
    <div class="role">Owner</div>
  </div>
  <div class="contact" style="position:absolute;left:104px;top:38px">
    3284-B Willow Crest Rd. #261<br>Greensboro, NC 27490<br><i></i>(336) 555-0142<br><i></i>verdalunenc@mailbox.example<br><i></i>www.VerdaLuneNC.example
  </div>
  <svg class="wave" viewBox="0 0 192 16" height="16" preserveAspectRatio="none"><path d="M0 10 Q60 0 192 6 V16 H0Z" fill="var(--green)"/></svg>
</div>

<!-- Card: back checklist green -->
<div class="item card" style="left:19px;top:168px;background:var(--green)">
  <div class="emblem" style="width:84px;height:84px;right:-14px;top:6px;background:rgba(255,255,255,.12)"></div>
  <ul class="checklist" style="position:absolute;left:12px;top:14px;color:#fff;columns:2;column-gap:12px;width:120px">
    <li>landscaping</li><li>hardscapes</li><li>lighting</li><li>irrigation</li><li>water features</li>
    <li>design</li><li>walls</li><li>patios</li><li>lawncare</li>
  </ul>
  <div class="web" style="position:absolute;left:12px;bottom:8px;color:#fff">www.VerdaLuneNC.example</div>
</div>

<!-- Card: back services dark -->
<div class="item card" style="left:228px;top:168px;background:var(--green-dark)">
  <div class="emblem" style="width:60px;height:60px;left:8px;top:4px;background:rgba(255,255,255,.1)"></div>
  <div class="wordmark" style="position:absolute;left:40px;top:12px;font-size:20px;color:#fff"><span class="dot" style="background:var(--green-light)"></span>VerdaLune</div>
  <div class="services" style="position:absolute;left:14px;top:44px;width:170px;text-align:center">
    landscaping | hardscapes | lighting | irrigation<br>water features | design | walls | patios<br>contract lawncare
  </div>
  <div class="web" style="position:absolute;left:0;right:0;bottom:7px;text-align:center;color:var(--green-light)">www.VerdaLuneNC.example</div>
</div>

<!-- Card: services white -->
<div class="item card" style="left:19px;top:271px">
  <div style="position:absolute;left:10px;top:8px">
    <div class="wordmark" style="font-size:17px"><span class="dot"></span>VerdaLune</div>
    <div class="tagline" style="margin:2px 0 0 17px">Landscape Management Services</div>
  </div>
  <div style="position:absolute;left:10px;top:44px;font-size:5px;line-height:8px;color:var(--green-dark)">
    landscaping | hardscapes | lighting | irrigation<br>water features | design | walls | patios | lawncare
  </div>
  <div class="web" style="position:absolute;left:10px;bottom:8px;color:var(--green)">www.VerdaLuneNC.example</div>
</div>

<!-- Card: emblem checklist white -->
<div class="item card" style="left:228px;top:271px">
  <div class="emblem" style="width:56px;height:56px;left:18px;top:20px;border:3px solid var(--green);background:var(--green-pale)"></div>
  <ul class="checklist" style="position:absolute;left:118px;top:10px;color:var(--green-dark)">
    <li>landscaping</li><li>hardscapes</li><li>lighting</li><li>irrigation</li><li>water features</li>
    <li>design</li><li>walls</li><li>patios</li><li>lawncare</li>
  </ul>
</div>

<!-- Letterhead -->
<div class="item" style="left:437px;top:36px;width:230px;height:444px">
  <div style="position:absolute;left:14px;top:14px">
    <div class="wordmark" style="font-size:17px"><span class="dot"></span>VerdaLune</div>
    <div class="tagline" style="margin:2px 0 0 17px">Landscape Management Services</div>
  </div>
  <div class="contact" style="position:absolute;left:150px;top:12px;font-size:4.2px;line-height:6.5px">
    3284-B Willow Crest Rd. #261<br>Greensboro, NC 27490<br><i></i>(336) 555-0187<br><i></i>verdalunenc@mailbox.example<br><i></i>www.VerdaLuneNC.example
  </div>
  <div class="emblem" style="width:130px;height:130px;left:58px;top:150px;border:2px solid var(--green-pale);background:rgba(159,204,122,.12)"></div>
  <svg class="wave" viewBox="0 0 230 30" height="30" preserveAspectRatio="none">
    <path d="M0 14 Q115 0 230 12 V30 H0Z" fill="var(--green-light)"/>
    <path d="M0 20 Q115 8 230 18 V30 H0Z" fill="var(--green)"/>
  </svg>
</div>

<!-- Envelope: back, top -->
<div class="item" style="left:720px;top:36px;width:312px;height:132px">
  <svg style="position:absolute;inset:0" viewBox="0 0 312 132" width="312" height="132">
    <path d="M0 0 L156 62 L312 0 Z" fill="var(--green-pale)"/>
    <path d="M0 0 L156 62 L312 0" fill="none" stroke="#ccc" stroke-width="1"/>
  </svg>
  <div class="emblem" style="width:28px;height:28px;left:142px;top:14px;background:var(--green)"></div>
</div>

<!-- Envelope: front -->
<div class="item" style="left:720px;top:122px;width:312px;height:140px">
  <div class="emblem" style="width:40px;height:40px;left:134px;top:10px;border:3px solid var(--green);background:var(--green-pale)"></div>
  <div class="wordmark" style="position:absolute;left:118px;top:58px;font-size:14px">VerdaLune</div>
  <svg style="position:absolute;inset:0" viewBox="0 0 312 140" width="312" height="140"><path d="M0 0 L156 40 L312 0" fill="none" stroke="#ddd"/></svg>
</div>

<!-- Envelope: front with green flap -->
<div class="item" style="left:679px;top:228px;width:312px;height:156px">
  <svg style="position:absolute;left:0;top:0" viewBox="0 0 312 60" width="312" height="60">
    <path d="M0 0 H312 L172 54 Q156 60 140 54 Z" fill="var(--green)"/>
  </svg>
  <div class="emblem" style="width:24px;height:24px;left:144px;top:16px;background:rgba(255,255,255,.35)"></div>
  <div style="position:absolute;left:12px;top:64px">
    <div class="wordmark" style="font-size:15px"><span class="dot"></span>VerdaLune</div>
    <div class="tagline" style="margin:2px 0 0 15px">Landscape Management Services</div>
    <div class="contact" style="margin-top:4px;font-size:4.2px;line-height:6px">3284-B Willow Crest Rd. #261<br>Greensboro, NC 27490</div>
  </div>
  <div class="emblem" style="width:90px;height:90px;left:180px;top:56px;background:rgba(159,204,122,.15)"></div>
  <svg class="wave" viewBox="0 0 312 14" height="14" preserveAspectRatio="none"><path d="M0 8 Q156 0 312 8 V14 H0Z" fill="var(--green)"/></svg>
</div>

</body>
</html>
```